PostPeddle Social Sharing Platform Needs a Redesign (2 pages / Design only)

PostPeddle is a popular social sharing platform for bloggers and marketers. The site has been quite popular for a few years now, but the site's design is looking quite dated. We're looking for a brand new design to give the service a facelift.

We are looking for a modern and fresh design that keeps all the existing functionality intact. Would prefer designs that incorporate the color blue in them.

We would like the two attached screenshots to be redesigned and submitted - using he same content. Please do not submit a redesign of the front page (non-logged in version). Redesign the 2 attached pages only, and the final deliverable is these two pages as layered PSD files.

Target Market(s)

bloggers, internet marketers

Industry/Entity Type

Social

Number of Pages Required

2 page

Requirements
Must have
• All existing functionality must be intact as seen from the screenshots.
Should not have
• Please do not submit designs based on existing front page (non-logged in version). Use attached screenshots (file 1 and 2) as a guide of existing functionality.

```html
<!DOCTYPE html>
<html lang="en">
<head>
<meta charset="utf-8">
<title>PostPeddle – My Timeline</title>
<link href="https://fonts.googleapis.com/css2?family=Open+Sans:wght@400;600;700&display=swap" rel="stylesheet">
<style>
:root{
  --blue:#1b80c8;
  --blue-link:#1a84c6;
  --orange:#f7941d;
  --dark:#2d2d2d;
  --darker:#1e1e1e;
  --panel-dark:#3b3b3b;
  --page:#f3f3f3;
  --white:#ffffff;
  --text:#333333;
  --muted:#8f8f8f;
  --line:#e3e3e3;
  --green:#2f9a3b;
  --fb:#3b5a98;
  --red:#d23f31;
}
*{box-sizing:border-box;margin:0;padding:0}
html,body{width:872px;height:1200px;overflow:hidden}
body{position:relative;background:var(--page);font-family:"Open Sans",Arial,sans-serif;color:var(--text);font-size:10px}
.abs{position:absolute}

/* header */
.site-header{left:0;top:0;width:872px;height:46px;background:var(--dark)}
.brand{left:68px;top:9px;display:flex;align-items:center;gap:7px;color:var(--white);font-size:22px;font-weight:600;letter-spacing:-.5px}
.brand-mark{width:14px;height:14px;background:var(--blue)}
.main-nav{left:392px;top:0;height:46px;display:flex;align-items:center;gap:15px;font-size:10px;font-weight:600;color:#8a8a8a}
.main-nav span{display:flex;align-items:center;gap:4px}
.main-nav .active{color:var(--white)}
.main-nav svg{width:11px;height:11px}

/* cover */
.cover{left:64px;top:57px;width:744px;height:163px}
.cover-photo{left:0;top:0;width:580px;height:163px;background:linear-gradient(100deg,#7d97ad 0%,#c9d2da 40%,#eef0f2 60%,#8f9caa 100%)}
.friend-grid{left:580px;top:0;width:164px;height:163px;display:grid;grid-template-columns:repeat(3,1fr);grid-template-rows:repeat(3,1fr);gap:1px;background:var(--white)}
.friend-grid .ph{background:linear-gradient(135deg,#c9a68a,#6d5446)}
.friend-grid .ph.alt{background:linear-gradient(135deg,#e2c39f,#8b6a50)}
.friend-grid .empty{background:#f4f4f4;display:flex;align-items:center;justify-content:center}
.profile-name{left:162px;top:184px;color:var(--white);font-size:19px}
.profile-bar{left:64px;top:220px;width:744px;height:38px;background:var(--white);border:1px solid var(--line);border-top:none}
.avatar-lg{left:85px;top:183px;width:70px;height:70px;border-radius:50%;border:3px solid var(--white);background:linear-gradient(135deg,#c79f80,#5a4032);box-shadow:0 0 0 1px #ccc}
.profile-tabs{left:104px;top:0;height:37px;display:flex;font-size:9px;color:#999}
.profile-tabs span{display:flex;align-items:center;gap:4px;padding:0 11px;border-right:1px solid var(--line)}
.profile-tabs .current{color:#555}
.profile-tabs svg{width:11px;height:11px}
.site-nav{left:374px;top:0;height:37px;display:flex;align-items:center;font-size:10.5px;color:#222}
.site-nav span{position:absolute;white-space:nowrap}

/* search */
.search-panel{left:64px;top:286px;width:480px;height:130px;background:var(--blue);border-radius:2px;color:var(--white);font-size:8.5px}
.select{height:23px;background:var(--white);color:#333;font-size:8.5px;display:flex;align-items:center;padding-left:11px;border-radius:2px}
.select::after{content:"";position:absolute;right:9px;top:7px;border:3px solid transparent;border-bottom-color:#333;box-shadow:0 0 0 0}
.select .arr{position:absolute;right:8px;top:6px;width:6px;height:11px}
.search-input{left:17px;top:85px;width:309px;height:20px;background:var(--white);border-radius:2px}
.search-btn{left:335px;top:85px;width:51px;height:20px;background:var(--orange);border-radius:2px;font-size:9px;font-weight:600;display:flex;align-items:center;justify-content:center}

/* posts */
.post{left:70px;width:474px;height:92px;background:var(--white);border:1px solid var(--line);border-radius:2px}
.post .thumb{left:17px;top:13px;width:51px;height:48px;background:linear-gradient(135deg,#8f8780,#2e2a28)}
.post .thumb.b{background:linear-gradient(135deg,#b99272,#3c3028)}
.post .meta{left:77px;top:13px;font-size:8.5px;color:var(--muted)}
.post .meta b{color:#444;font-weight:700}
.post .meta em{font-style:normal;color:#444}
.post .body{left:77px;top:28px;width:360px;font-size:9.6px;line-height:12px;color:#222}
.post .body a{color:var(--blue-link);text-decoration:none}
.actions{left:26px;top:71px;display:flex;align-items:center;font-size:8.5px;font-weight:700;color:var(--blue-link);height:14px}
.actions .act{display:flex;align-items:center;gap:3px;margin-right:20px}
.actions svg{width:9px;height:9px}
.like{display:flex;align-items:center;height:13px}
.like .btn{background:var(--fb);color:var(--white);font-size:7.5px;padding:0 5px;height:13px;display:flex;align-items:center;border-radius:2px}
.share .btn{background:var(--white);color:var(--red);border:1px solid #ccc}
.count{height:13px;border:1px solid #c9c9c9;font-size:7px;color:#555;font-weight:400;padding:0 4px;display:flex;align-items:center;margin-left:3px;border-radius:2px}

/* comments widget */
.comments{left:566px;top:286px;width:240px;height:302px;background:var(--white);border:1px solid var(--line)}
.comments-head{left:0;top:0;width:240px;height:32px;background:var(--blue);color:var(--white)}
.comments-head .av{left:0;top:0;width:32px;height:32px;background:linear-gradient(135deg,#e8d2a6,#9b7b58)}
.comments-head .who{left:42px;top:4px;font-size:9.5px;font-weight:700}
.comments-head .when{left:42px;top:17px;font-size:9px}
.comments-head svg{position:absolute;right:8px;top:9px;width:18px;height:13px}
.album-title{left:9px;top:41px;font-size:9px;color:#333}
.album{top:62px;width:66px;height:66px}
.view-all{left:4px;top:140px;font-size:7.5px;color:#444;display:flex;align-items:center;gap:3px}
.view-all span{color:#aaa}
.c-row{left:0;width:240px;height:40px;border-top:1px solid var(--line)}
.c-row .av{left:4px;top:5px;width:32px;height:32px;background:linear-gradient(135deg,#b48d70,#3a2c24)}
.c-row .av.f{background:linear-gradient(135deg,#e8d2a6,#9b7b58)}
.c-row .txt{left:42px;top:6px;font-size:8.5px;color:#333}
.c-row .txt span{color:var(--blue-link)}
.c-row .time{left:42px;top:19px;font-size:7.5px;color:#888}
.c-input{left:3px;top:278px;width:208px;height:20px;background:#f5f5f5;border:1px solid #e6e6e6}
.c-photo{left:211px;top:278px;width:25px;height:20px;border:1px solid #e6e6e6;display:flex;align-items:center;justify-content:center}

/* why signup */
.signup{left:566px;top:608px;width:237px;height:336px;background:var(--white);box-shadow:0 1px 2px rgba(0,0,0,.1)}
.signup-head{left:0;top:0;width:237px;height:52px;background:var(--panel-dark);border-bottom:3px solid #e8542e;color:var(--white);font-size:13px;display:flex;align-items:center;gap:12px;padding-left:20px}
.member{left:15px;width:208px;height:72px;border-bottom:1px dashed #d9d9d9}
.member .ph{left:10px;top:8px;width:56px;height:56px;border-radius:50%;border:3px solid #eee;box-shadow:0 0 0 1px #ccc;background:radial-gradient(circle at 50% 45%,#d8b995,#7a5633)}
.member .nm{left:77px;top:20px;font-size:13px;color:var(--blue-link)}
.member .yr{left:77px;top:38px;font-size:9px;color:#bbb;font-weight:600;letter-spacing:.5px}
.signup-foot{left:0;top:298px;width:237px;height:38px;border-top:1px solid var(--line);font-size:9px;color:#999;font-weight:600;padding-left:17px;display:flex;align-items:center}

/* footer */
.site-footer{left:0;top:969px;width:872px;height:185px;background:#2a2a2a}
.f-col h3{font-size:13px;font-weight:700;color:var(--blue-link);margin-bottom:11px}
.f-col ul{list-style:none}
.f-col li{font-size:8.8px;color:#bbb;letter-spacing:.5px;height:17.6px;display:flex;align-items:center;gap:7px}
.f-col li::before{content:"";width:4px;height:4px;border-radius:50%;background:var(--blue-link)}
.f-col .addr{font-size:8.8px;color:#bbb;letter-spacing:.5px;line-height:17.6px}
.map{left:557px;top:11px;width:233px;height:165px;border:3px solid var(--white);background:linear-gradient(135deg,#ede5c6,#f4efdc 50%,#e7ddb9)}
.bottom-bar{left:0;top:1154px;width:872px;height:46px;background:var(--darker);color:var(--white);font-size:8.5px;font-weight:600}
.bottom-nav span{position:absolute;top:10px;white-space:nowrap}
.copyright{left:0;width:872px;top:30px;text-align:center;font-weight:400;font-size:8.8px}
</style>
</head>
<body>

<header class="abs site-header">
  <div class="abs brand"><span class="brand-mark"></span>PostPeddle</div>
  <nav class="abs main-nav">
    <span class="active"><svg viewBox="0 0 12 12"><circle cx="6" cy="6" r="4" fill="none" stroke="#fff" stroke-width="2"/><circle cx="6" cy="6" r="1.5" fill="#fff"/></svg>My Timeline</span>
    <span><svg viewBox="0 0 12 12"><circle cx="6" cy="6" r="5" fill="none" stroke="#8a8a8a" stroke-width="1.2"/><circle cx="6" cy="5" r="2" fill="#8a8a8a"/></svg>Edit Profile</span>
    <span><svg viewBox="0 0 12 12"><circle cx="4" cy="4" r="2.2" fill="#8a8a8a"/><circle cx="8.5" cy="4" r="2.2" fill="#8a8a8a"/><rect x="1" y="7" width="10" height="4" rx="2" fill="#8a8a8a"/></svg>Manage Friends</span>
    <span><svg viewBox="0 0 12 12"><ellipse cx="6" cy="5.5" rx="5" ry="4.5" fill="#8a8a8a"/></svg>Messages</span>
    <span>Logout <svg viewBox="0 0 12 12"><rect x="2" y="5" width="8" height="6" fill="#8a8a8a"/><path d="M4 5V3a2 2 0 0 1 4 0" fill="none" stroke="#8a8a8a" stroke-width="1.2"/></svg></span>
  </nav>
</header>

<section class="abs cover">
  <div class="abs cover-photo" role="img" aria-label="Cover photo: businesswoman holding a phone and documents"></div>
  <div class="abs friend-grid">
    <div class="ph" role="img" aria-label="Friend photo"></div>
    <div class="ph alt" role="img" aria-label="Friend photo"></div>
    <div class="ph" role="img" aria-label="Friend photo"></div>
    <div class="ph" role="img" aria-label="Friend photo"></div>
    <div class="ph alt" role="img" aria-label="Friend photo"></div>
    <div class="ph" role="img" aria-label="Friend photo"></div>
    <div class="ph" role="img" aria-label="Friend photo"></div>
    <div class="ph alt" role="img" aria-label="Friend photo"></div>
    <div class="empty"><svg width="30" height="22" viewBox="0 0 30 22"><circle cx="8" cy="7" r="4" fill="#ddd"/><circle cx="22" cy="7" r="4" fill="#ddd"/><circle cx="15" cy="6" r="5" fill="#e4e4e4"/><rect x="6" y="12" width="18" height="9" rx="4" fill="#e4e4e4"/></svg></div>
  </div>
</section>
<div class="abs profile-name">Dan Morrow</div>

<div class="abs profile-bar">
  <div class="abs profile-tabs">
    <span class="current"><svg viewBox="0 0 12 12"><circle cx="6" cy="6" r="4" fill="none" stroke="#666" stroke-width="2"/><circle cx="6" cy="6" r="1.5" fill="#666"/></svg>Timeline</span>
    <span><svg viewBox="0 0 12 12"><circle cx="6" cy="6" r="5" fill="none" stroke="#bbb"/><circle cx="6" cy="5" r="2" fill="#bbb"/></svg>About</span>
    <span><svg viewBox="0 0 12 12"><circle cx="4" cy="4" r="2.2" fill="#bbb"/><circle cx="8.5" cy="4" r="2.2" fill="#bbb"/><rect x="1" y="7" width="10" height="4" rx="2" fill="#bbb"/></svg>Friends</span>
  </div>
  <nav class="abs site-nav">
    <span style="left:0;top:13px">DASHBOARD</span>
    <span style="left:94px;top:13px">HOW IT WORKS</span>
    <span style="left:208px;top:13px">CONTACT US</span>
    <span style="left:316px;top:13px">BLOG</span>
  </nav>
</div>
<div class="abs avatar-lg" role="img" aria-label="Profile photo of Dan Morrow"></div>

<section class="abs search-panel">
  <div class="abs" style="left:13px;top:19px">Order by :</div>
  <div class="abs select" style="left:56px;top:8px;width:170px"><svg class="arr" viewBox="0 0 6 11"><path d="M0 4L3 1L6 4M0 7L3 10L6 7" fill="none" stroke="#333" stroke-width="1.2"/></svg></div>
  <div class="abs select" style="left:240px;top:8px;width:206px">All categories<svg class="arr" viewBox="0 0 6 11"><path d="M0 4L3 1L6 4M0 7L3 10L6 7" fill="none" stroke="#333" stroke-width="1.2"/></svg></div>
  <div class="abs" style="left:17px;top:64px">Search (Keyword or Chirper handle)</div>
  <div class="abs search-input"></div>
  <div class="abs search-btn">SEARCH</div>
</section>

<!-- feed -->
<article class="abs post" style="top:442px">
  <div class="abs thumb" role="img" aria-label="Member photo"></div>
  <div class="abs meta"><b>@brightpixelworks</b> is offering 5 credits to promote this &nbsp;<em>(Blogware)</em></div>
  <p class="abs body">Tip #1 for a new #Blogware blog - make your archive searchable by topic instead of date. #blogging <a>http://brightpixelworks.com/idea-15</a></p>
  <div class="abs actions">
    <span class="act"><svg viewBox="0 0 10 10"><path d="M5 0.5L9.7 9.5H0.3Z" fill="#f5b400"/><rect x="4.5" y="3.5" width="1" height="3" fill="#fff"/></svg>Report Tweet</span>
    <span class="act"><svg viewBox="0 0 10 10"><path d="M2 5h4M5 2.5L8 5L5 7.5" fill="none" stroke="#2f9a3b" stroke-width="1.6"/></svg>Skip this</span>
    <span class="act"><svg viewBox="0 0 10 10"><path d="M1.5 4A3.5 3.5 0 0 1 8 3M8.5 6A3.5 3.5 0 0 1 2 7" fill="none" stroke="#1a84c6" stroke-width="1.3"/></svg>Schedule Retweet</span>
    <span class="like"><span class="btn">Like</span><span class="count">11</span></span>
    <span class="like share" style="margin-left:20px"><span class="btn">Share</span><span class="count">6</span></span>
  </div>
</article>

<article class="abs post" style="top:545px">
  <div class="abs thumb b" role="img" aria-label="Member photo"></div>
  <div class="abs meta"><b>@brightpixelworks</b> is offering 5 credits to promote this &nbsp;<em>(Blogware)</em></div>
  <p class="abs body">Tip #1 for a new #Blogware blog - make your archive searchable by topic instead of date. #blogging <a>http://brightpixelworks.com/idea-15</a></p>
  <div class="abs actions">
    <span class="act"><svg viewBox="0 0 10 10"><path d="M5 0.5L9.7 9.5H0.3Z" fill="#f5b400"/><rect x="4.5" y="3.5" width="1" height="3" fill="#fff"/></svg>Report Tweet</span>
    <span class="act"><svg viewBox="0 0 10 10"><path d="M2 5h4M5 2.5L8 5L5 7.5" fill="none" stroke="#2f9a3b" stroke-width="1.6"/></svg>Skip this</span>
    <span class="act"><svg viewBox="0 0 10 10"><path d="M1.5 4A3.5 3.5 0 0 1 8 3M8.5 6A3.5 3.5 0 0 1 2 7" fill="none" stroke="#1a84c6" stroke-width="1.3"/></svg>Schedule Retweet</span>
    <span class="like"><span class="btn">Like</span><span class="count">11</span></span>
    <span class="like share" style="margin-left:20px"><span class="btn">Share</span><span class="count">6</span></span>
  </div>
</article>

<article class="abs post" style="top:649px">
  <div class="abs thumb" role="img" aria-label="Member photo"></div>
  <div class="abs meta"><b>@brightpixelworks</b> is offering 5 credits to promote this &nbsp;<em>(Blogware)</em></div>
  <p class="abs body">Tip #1 for a new #Blogware blog - make your archive searchable by topic instead of date. #blogging <a>http://brightpixelworks.com/idea-15</a></p>
  <div class="abs actions">
    <span class="act"><svg viewBox="0 0 10 10"><path d="M5 0.5L9.7 9.5H0.3Z" fill="#f5b400"/><rect x="4.5" y="3.5" width="1" height="3" fill="#fff"/></svg>Report Tweet</span>
    <span class="act"><svg viewBox="0 0 10 10"><path d="M2 5h4M5 2.5L8 5L5 7.5" fill="none" stroke="#2f9a3b" stroke-width="1.6"/></svg>Skip this</span>
    <span class="act"><svg viewBox="0 0 10 10"><path d="M1.5 4A3.5 3.5 0 0 1 8 3M8.5 6A3.5 3.5 0 0 1 2 7" fill="none" stroke="#1a84c6" stroke-width="1.3"/></svg>Schedule Retweet</span>
    <span class="like"><span class="btn">Like</span><span class="count">11</span></span>
    <span class="like share" style="margin-left:20px"><span class="btn">Share</span><span class="count">6</span></span>
  </div>
</article>

<article class="abs post" style="top:749px">
  <div class="abs thumb b" role="img" aria-label="Member photo"></div>
  <div class="abs meta"><b>@brightpixelworks</b> is offering 5 credits to promote this &nbsp;<em>(Blogware)</em></div>
  <p class="abs body">Tip #1 for a new #Blogware blog - make your archive searchable by topic instead of date. #blogging <a>http://brightpixelworks.com/idea-15</a></p>
  <div class="abs actions">
    <span class="act"><svg viewBox="0 0 10 10"><path d="M5 0.5L9.7 9.5H0.3Z" fill="#f5b400"/><rect x="4.5" y="3.5" width="1" height="3" fill="#fff"/></svg>Report Tweet</span>
    <span class="act"><svg viewBox="0 0 10 10"><path d="M2 5h4M5 2.5L8 5L5 7.5" fill="none" stroke="#2f9a3b" stroke-width="1.6"/></svg>Skip this</span>
    <span class="act"><svg viewBox="0 0 10 10"><path d="M1.5 4A3.5 3.5 0 0 1 8 3M8.5 6A3.5 3.5 0 0 1 2 7" fill="none" stroke="#1a84c6" stroke-width="1.3"/></svg>Schedule Retweet</span>
    <span class="like"><span class="btn">Like</span><span class="count">11</span></span>
    <span class="like share" style="margin-left:20px"><span class="btn">Share</span><span class="count">6</span></span>
  </div>
</article>

<article class="abs post" style="top:853px">
  <div class="abs thumb" role="img" aria-label="Member photo"></div>
  <div class="abs meta"><b>@brightpixelworks</b> is offering 5 credits to promote this &nbsp;<em>(Blogware)</em></div>
  <p class="abs body">Tip #1 for a new #Blogware blog - make your archive searchable by topic instead of date. #blogging <a>http://brightpixelworks.com/idea-15</a></p>
  <div class="abs actions">
    <span class="act"><svg viewBox="0 0 10 10"><path d="M5 0.5L9.7 9.5H0.3Z" fill="#f5b400"/><rect x="4.5" y="3.5" width="1" height="3" fill="#fff"/></svg>Report Tweet</span>
    <span class="act"><svg viewBox="0 0 10 10"><path d="M2 5h4M5 2.5L8 5L5 7.5" fill="none" stroke="#2f9a3b" stroke-width="1.6"/></svg>Skip this</span>
    <span class="act"><svg viewBox="0 0 10 10"><path d="M1.5 4A3.5 3.5 0 0 1 8 3M8.5 6A3.5 3.5 0 0 1 2 7" fill="none" stroke="#1a84c6" stroke-width="1.3"/></svg>Schedule Retweet</span>
    <span class="like"><span class="btn">Like</span><span class="count">11</span></span>
    <span class="like share" style="margin-left:20px"><span class="btn">Share</span><span class="count">6</span></span>
  </div>
</article>

<!-- sidebar: comments -->
<aside class="abs comments">
  <div class="abs comments-head">
    <div class="abs av" role="img" aria-label="Photo of Nora"></div>
    <div class="abs who">Nora</div>
    <div class="abs when">on 15th January, 2014</div>
    <svg viewBox="0 0 18 13"><path d="M7 1L1 6L7 11V8C11 8 14 9 17 12C16 7 13 4 7 4Z" fill="#fff"/></svg>
  </div>
  <div class="abs album-title">Late Night Show Photos</div>
  <div class="abs album" style="left:9px;background:linear-gradient(135deg,#d9a47c,#7a3e24)" role="img" aria-label="Party photo"></div>
  <div class="abs album" style="left:78px;background:linear-gradient(135deg,#3d6fd1,#1a2c6e)" role="img" aria-label="Party photo"></div>
  <div class="abs album" style="left:146px;background:linear-gradient(135deg,#6b4a2f,#1a120c)" role="img" aria-label="Party photo"></div>
  <div class="abs view-all"><svg width="8" height="7" viewBox="0 0 8 7"><ellipse cx="4" cy="3" rx="3.5" ry="2.5" fill="none" stroke="#555"/></svg>View all <span>10 comments</span></div>
  <div class="abs c-row" style="top:153px"><div class="abs av" role="img" aria-label="Photo of Dan M."></div><div class="abs txt"><span>Dan M.</span> Hi Nora, Nice Party</div><div class="abs time">21st September</div></div>
  <div class="abs c-row" style="top:193px"><div class="abs av f" role="img" aria-label="Photo of Nora"></div><div class="abs txt"><span>Nora</span> Thanks Dan</div><div class="abs time">2 days</div></div>
  <div class="abs c-row" style="top:233px"><div class="abs av" role="img" aria-label="Photo of Dan M."></div><div class="abs txt"><span>Dan M.</span> What time did it finish?</div><div class="abs time">14 min</div></div>
  <div class="abs c-input"></div>
  <div class="abs c-photo"><svg width="11" height="9" viewBox="0 0 11 9"><rect x=".5" y=".5" width="10" height="8" fill="none" stroke="#1a9e8a"/><path d="M1 8L4 4L6 6L8 3.5L10 8Z" fill="#1a9e8a"/></svg></div>
</aside>

<!-- sidebar: why signup -->
<aside class="abs signup">
  <div class="abs signup-head"><svg width="22" height="22" viewBox="0 0 22 22"><rect x="1.5" y="3.5" width="19" height="17" fill="none" stroke="#fff" stroke-width="1.6"/><line x1="1.5" y1="8" x2="20.5" y2="8" stroke="#fff" stroke-width="1.6"/><rect x="5" y="1" width="2" height="4" fill="#fff"/><rect x="15" y="1" width="2" height="4" fill="#fff"/><g fill="#fff"><rect x="5" y="11" width="2" height="2"/><rect x="10" y="11" width="2" height="2"/><rect x="15" y="11" width="2" height="2"/><rect x="5" y="15" width="2" height="2"/><rect x="10" y="15" width="2" height="2"/><rect x="15" y="15" width="2" height="2"/></g></svg>Why Signup?</div>
  <div class="abs member" style="top:64px"><div class="abs ph" role="img" aria-label="Member portrait"></div><div class="abs nm">Alan Porter</div><div class="abs yr">1890-1970</div></div>
  <div class="abs member" style="top:136px"><div class="abs ph" role="img" aria-label="Member portrait"></div><div class="abs nm">Alan Porter</div><div class="abs yr">1890-1970</div></div>
  <div class="abs member" style="top:208px;border-bottom:none;height:80px"><div class="abs ph" style="top:16px" role="img" aria-label="Member portrait"></div><div class="abs nm" style="top:28px">Alan Porter</div><div class="abs yr" style="top:46px">1890-1970</div></div>
  <div class="abs signup-foot">VIEW ALL &nbsp;→</div>
</aside>

<!-- footer -->
<footer class="abs site-footer">
  <div class="abs f-col" style="left:98px;top:17px">
    <h3>CATEGORIES</h3>
    <ul><li>Did You Know?</li><li>Treasury Fundamentals</li><li>60 Second Lessons</li><li>Recommend</li><li>About</li></ul>
  </div>
  <div class="abs f-col" style="left:262px;top:17px">
    <h3>POLICIES</h3>
    <ul><li>Privacy Policy</li><li>Affiliate Disclaimer</li><li>Copyright</li><li>External Link Policy</li><li>Anti Spam Policy</li><li>DCMA Disclaimer</li></ul>
  </div>
  <div class="abs f-col" style="left:418px;top:17px">
    <h3>ADDRESS</h3>
    <p class="addr">418 Alder Lane<br>Suite 210<br>Brookfield, NC 27500</p>
  </div>
  <div class="abs map" role="img" aria-label="Street map showing the office location"></div>
</footer>

<div class="abs bottom-bar">
  <nav class="bottom-nav">
    <span style="left:107px">HOME</span>
    <span style="left:161px">ABOUT US</span>
    <span style="left:232px">THE TEAM</span>
    <span style="left:303px">RESUME TIPS</span>
    <span style="left:388px">TIMESHEETS</span>
    <span style="left:470px">SEND RESUME</span>
    <span style="left:560px">CANDIDATES</span>
    <span style="left:642px">LOCATION</span>
    <span style="left:713px">CONTACT US</span>
  </nav>
  <div class="abs copyright">© 2012 postpeddle - The Hiring Hall</div>
</div>

</body>
</html>
```